Pebble and Pine App design

I need a full app design, colours, images, fonts, and a mock up design of the app to bring to the developer.

Pebble and Pine is a free app that allows cafes, independent cafe and chains of cafes to let their customers know what the soup of the day and what specials they have on that day through the app. Each cafe will have a profile which they can upload the Pebble and Pine daily.

The user home screen will include google maps showing their location with the registered cafes and eateries around them. including a list of the cafe and distances below. as seen in attachment.

Target Market(s)

Cafes , anyone who enjoys eating soups and off local cafe specials boards

Requirements
Must have
• I would like a complete app design based on the attached images.

```html
<!DOCTYPE html>
<html lang="en">
<head>
<meta charset="utf-8">
<title>Pebble and Pine – App Screens</title>
<link href="https://fonts.googleapis.com/css2?family=Roboto:wght@300;400;500;700&display=swap" rel="stylesheet">
<style>
:root{
  --orange:#fb8c15;
  --orange-soft:#fda449;
  --bg:#ffffff;
  --screen:#f6f6f6;
  --card:#ffffff;
  --ink:#1f1f1f;
  --muted:#8a8a8a;
  --line:#e3e3e3;
  --star:#f5a623;
  --go:#1ed61e;
  --stop:#e4141b;
}
*{box-sizing:border-box;margin:0;padding:0}
html,body{width:1200px;height:1200px;overflow:hidden;background:var(--bg);font-family:"Roboto",sans-serif;color:var(--ink)}
.canvas{position:relative;width:1200px;height:1200px}
.screen{position:absolute;width:224px;height:478px;background:var(--screen);border-radius:26px;overflow:hidden;box-shadow:0 0 0 1px #ececec}
.status{position:absolute;top:12px;left:18px;right:16px;display:flex;justify-content:space-between;align-items:center;font-size:9px;font-weight:500}
.status-icons{display:flex;gap:3px;align-items:center}
.status-icons svg{height:7px;fill:var(--ink)}
.pill{position:absolute;left:10px;right:10px;height:22px;border-radius:11px;background:var(--orange);color:#fff;font-size:8px;font-weight:400;line-height:22px;padding-left:11px;letter-spacing:.1px}
.pill svg{position:absolute;right:10px;top:6px;width:10px;height:10px;stroke:#fff;fill:none;stroke-width:1.6}
.heading{position:absolute;left:10px;font-size:8px;font-weight:400;letter-spacing:.1px}
.map{position:absolute;left:10px;right:10px;border-radius:6px;background:linear-gradient(135deg,#eceff1 0%,#e6e9ec 45%,#d7ead0 70%,#e9ece9 100%)}
.item{position:absolute;left:10px;width:202px;height:65px;background:var(--card);border-radius:6px;box-shadow:0 2px 5px rgba(0,0,0,.12);display:flex;overflow:hidden}
.item-photo{width:65px;flex:none}
.item-info{padding:8px 0 0 12px;position:relative;flex:1}
.item-name{font-size:7px;font-weight:500}
.item-place{font-size:4.5px;color:var(--muted);margin-top:1px}
.item-rating{font-size:4px;color:var(--muted);margin-top:5px}
.item-rating b{color:var(--ink);font-weight:700}
.star{color:var(--star)}
.item-price{position:absolute;left:12px;top:47px;font-size:9px;font-weight:400;color:#444}
.fav{position:absolute;right:9px;top:7px;width:12px;height:11px;fill:none;stroke:#cfcfcf;stroke-width:1.4}
.fav.on{fill:var(--orange);stroke:var(--orange)}
.dot{position:absolute;right:14px;bottom:10px;width:4px;height:4px;border-radius:50%}
.dot.go{background:var(--go)}
.dot.stop{background:var(--stop)}
.tone-a{background:radial-gradient(circle at 40% 55%,#e0741a 0%,#b04a12 45%,#3a1f12 100%)}
.tone-b{background:radial-gradient(circle at 45% 60%,#d97b24 0%,#7a4a2a 40%,#3d5268 75%,#2b3440 100%)}
.tone-c{background:radial-gradient(circle at 45% 45%,#ef7a2c 0%,#a8522a 30%,#2c4a48 60%,#1c2b2c 100%)}
.tone-d{background:radial-gradient(circle at 50% 50%,#c53a1c 0%,#7a2a18 30%,#2b3238 60%,#1a1e22 100%)}
.tone-e{background:radial-gradient(circle at 50% 50%,#efe9dc 0%,#d9cdb8 40%,#b9aa92 70%,#eeeae4 100%)}
.tone-cafe{background:linear-gradient(160deg,#3a2d22 0%,#6b4a2c 40%,#2a241e 70%,#a67c4c 100%)}
.tone-street{background:linear-gradient(170deg,#c9b49a 0%,#8f6c4a 40%,#4a3524 70%,#a48e76 100%)}
.est{position:absolute;height:64px;background:var(--card);border-radius:6px;box-shadow:0 2px 5px rgba(0,0,0,.12);display:flex;overflow:hidden}
.est-photo{width:64px;flex:none}
.est-info{position:relative;flex:1;padding:6px 0 0 6px}
.est-name{font-size:7px;font-weight:500}
.est-place{font-size:4.5px;color:var(--muted);margin-top:1px}
.est-dist{position:absolute;left:6px;top:44px;font-size:4px;color:#555;display:flex;align-items:center;gap:1px}
.est-dist svg{width:4px;height:5px;fill:none;stroke:#555;stroke-width:1}
.est-stars{position:absolute;left:6px;top:51px;font-size:4.5px;color:var(--star);letter-spacing:.5px}
.est-price{position:absolute;right:6px;top:48px;font-size:8px;color:#444}
.tabs{position:absolute;top:368px;left:10px;right:4px;display:flex;justify-content:space-between;font-size:8px}
.tabs .active{color:var(--orange);border-bottom:1.5px solid var(--orange);padding-bottom:2px}
.promo{position:absolute;top:394px;width:74px;height:118px;border-radius:8px;background:var(--orange);color:#fff;overflow:hidden;padding:8px 8px}
.promo-title{font-size:4.8px;font-weight:500}
.promo-text{font-size:2.8px;line-height:1.5;margin-top:3px;opacity:.9}
.promo-price{font-size:8px;margin-top:7px}
.promo-bowl{position:absolute;left:1px;right:1px;top:78px;height:74px;border-radius:50%;background:radial-gradient(circle at 50% 45%,#e29a2a 0%,#c06c18 45%,#8a5a2c 65%,#f2efe9 68%)}
.tabbar{position:absolute;left:0;right:0;bottom:0;height:30px;background:var(--orange);display:flex;justify-content:space-around;align-items:center;padding:0 8px}
.tabbar svg{width:11px;height:11px;fill:none;stroke:#fff;stroke-width:1.4}
.tabbar .gap{width:11px}
.raised{position:absolute;width:34px;height:34px;border-radius:50%;background:var(--orange);border:3px solid #fff;display:flex;align-items:center;justify-content:center;box-shadow:0 1px 4px rgba(0,0,0,.15)}
.raised svg{width:14px;height:14px;fill:none;stroke:#fff;stroke-width:1.4}
.hero{position:absolute;left:10px;right:10px;top:72px;height:105px;border-radius:8px}
.pager{position:absolute;top:187px;left:0;right:0;display:flex;justify-content:center;gap:3px}
.pager span{height:1.5px;width:4px;background:#ccc;border-radius:1px}
.pager span.on{width:11px;background:var(--orange)}
.info{position:absolute;left:10px;right:10px;top:197px;height:56px;background:var(--card);border-radius:6px;box-shadow:0 2px 5px rgba(0,0,0,.1);padding:9px 12px;font-size:6.5px;font-weight:500;color:#444;line-height:14px}
.group{position:absolute;left:10px;font-size:7px;font-weight:500;display:flex;align-items:center;gap:4px}
.group svg{width:5px;height:4px;fill:none;stroke:var(--ink);stroke-width:1.2}
.row{position:absolute;left:10px;width:202px;height:32px;background:var(--card);border-radius:4px;box-shadow:0 2px 4px rgba(0,0,0,.1);display:flex;align-items:center}
.row-photo{width:32px;height:32px;flex:none;border-radius:4px 0 0 4px}
.row-info{flex:1;padding-left:7px}
.row-name{font-size:6.5px;font-weight:500}
.row-qty{font-size:6px;color:var(--orange);margin-top:5px}
.row-price{font-size:9px;font-weight:500;padding-right:8px}
</style>
</head>
<body>
<svg width="0" height="0" style="position:absolute" aria-hidden="true">
  <defs>
    <symbol id="i-home" viewBox="0 0 24 24"><path d="M3 11 12 3l9 8v10h-6v-6H9v6H3z"/></symbol>
    <symbol id="i-search" viewBox="0 0 24 24"><circle cx="14" cy="10" r="6.5"/><path d="M9.5 14.5 3 21"/></symbol>
    <symbol id="i-bowl" viewBox="0 0 24 24"><circle cx="12" cy="12" r="9"/><circle cx="12" cy="12" r="5.5"/><circle cx="10" cy="11" r=".8"/><circle cx="14" cy="13" r=".8"/><path d="M17 3l-3 5"/></symbol>
    <symbol id="i-heart" viewBox="0 0 24 22"><path d="M12 20S2 13.5 2 7.2A5 5 0 0 1 12 5a5 5 0 0 1 10 2.2C22 13.5 12 20 12 20z"/></symbol>
    <symbol id="i-gear" viewBox="0 0 24 24"><circle cx="12" cy="12" r="3.5"/><path d="M12 2.5l1.6 2.6 3-.8.8 3 2.6 1.6-1.4 2.8 1.4 2.8-2.6 1.6-.8 3-3-.8L12 21.5l-1.6-2.6-3 .8-.8-3L4 15.1l1.4-2.8L4 9.5l2.6-1.6.8-3 3 .8z"/></symbol>
    <symbol id="i-pin" viewBox="0 0 8 10"><path d="M4 9.5S.8 6 .8 3.8a3.2 3.2 0 0 1 6.4 0C7.2 6 4 9.5 4 9.5z"/><circle cx="4" cy="3.8" r="1"/></symbol>
    <symbol id="i-signal" viewBox="0 0 34 10"><rect x="0" y="7" width="2" height="3"/><rect x="3" y="5" width="2" height="5"/><rect x="6" y="3" width="2" height="7"/><rect x="9" y="1" width="2" height="9"/><path d="M14 4.5a6 6 0 0 1 8 0l-1 1a4.5 4.5 0 0 0-6 0zM16 6.6a3 3 0 0 1 4 0L18 8.6z"/><rect x="24" y="2" width="10" height="6" rx="1.5"/></symbol>
  </defs>
</svg>

<main class="canvas">

  <!-- Home: map and nearby cafes -->
  <section class="screen" style="left:138px;top:75px">
    <div class="status"><span>9:41</span><span class="status-icons"><svg viewBox="0 0 34 10" width="26"><use href="#i-signal"/></svg></span></div>
    <div class="pill" style="top:34px">SEARCH LOCATION<svg viewBox="0 0 24 24"><use href="#i-search"/></svg></div>
    <div class="map" style="top:72px;height:105px" role="img" aria-label="Street map showing the user's location and nearby cafes"></div>
    <p class="heading" style="top:191px">LIST OF NEAR ESTABLISHMENT</p>
    <div class="est" style="left:10px;top:215px;width:160px">
      <div class="est-photo tone-cafe" role="img" aria-label="Cafe interior"></div>
      <div class="est-info">
        <p class="est-name">Cafe Copper Pot</p>
        <p class="est-place">Old Town, Spain</p>
        <p class="est-dist"><svg viewBox="0 0 8 10"><use href="#i-pin"/></svg>2 km to cafe</p>
        <p class="est-stars">★★★★★</p>
        <p class="est-price">$ 8.00</p>
      </div>
    </div>
    <div class="est" style="left:180px;top:215px;width:60px">
      <div class="est-photo tone-street" role="img" aria-label="Cafe terrace on a street"></div>
    </div>
    <nav class="tabs" style="top:292px"><span class="active">SOUP</span><span>MENU</span><span>DRINK</span><span>DESSERT</span></nav>
    <div class="promo" style="left:10px;top:318px">
      <p class="promo-title">THE POWER OF SOUP</p>
      <p class="promo-text">Hearty bowls made fresh each morning with local greens, slow broth and warm spices.</p>
      <p class="promo-price">8.00</p>
      <div class="promo-bowl" role="img" aria-label="Bowl of lentil soup"></div>
    </div>
    <div class="promo" style="left:96px;top:318px">
      <p class="promo-title">THE POWER OF SOUP</p>
      <p class="promo-text">Hearty bowls made fresh each morning with local greens, slow broth and warm spices.</p>
      <p class="promo-price">8.00</p>
      <div class="promo-bowl" role="img" aria-label="Bowl of lentil soup"></div>
    </div>
    <div class="promo" style="left:182px;top:318px">
      <p class="promo-title">THE POWER OF SOUP</p>
      <p class="promo-text">Hearty bowls made fresh each morning with local greens, slow broth and warm spices.</p>
      <p class="promo-price">8.00</p>
      <div class="promo-bowl" role="img" aria-label="Bowl of lentil soup"></div>
    </div>
    <nav class="tabbar"><span class="gap"></span><svg viewBox="0 0 24 24"><use href="#i-search"/></svg><svg viewBox="0 0 24 24"><use href="#i-bowl"/></svg><svg viewBox="0 0 24 22"><use href="#i-heart"/></svg><svg viewBox="0 0 24 24"><use href="#i-gear"/></svg></nav>
    <div class="raised" style="left:13px;top:423px"><svg viewBox="0 0 24 24"><use href="#i-home"/></svg></div>
  </section>

  <!-- Soup list -->
  <section class="screen" style="left:494px;top:75px">
    <div class="status"><span>9:41</span><span class="status-icons"><svg viewBox="0 0 34 10" width="26"><use href="#i-signal"/></svg></span></div>
    <div class="pill" style="top:34px">SOUP NAME</div>
    <div class="item" style="top:72px"><div class="item-photo tone-a" role="img" aria-label="Vegetable stew with potatoes"></div><div class="item-info"><p class="item-name">Ladle House</p><p class="item-place">Old Town, Spain</p><p class="item-rating"><span class="star">★</span> <b>5.0</b> (210 ratings)</p><p class="item-price">$ 8.00</p></div><svg class="fav" viewBox="0 0 24 22"><use href="#i-heart"/></svg></div>
    <div class="item" style="top:146px"><div class="item-photo tone-b" role="img" aria-label="Bowl of pumpkin soup with bread"></div><div class="item-info"><p class="item-name">Ladle House</p><p class="item-place">Old Town, Spain</p><p class="item-rating"><span class="star">★</span> <b>5.0</b> (210 ratings)</p><p class="item-price">$ 12.00</p></div><svg class="fav on" viewBox="0 0 24 22"><use href="#i-heart"/></svg></div>
    <div class="item" style="top:220px"><div class="item-photo tone-c" role="img" aria-label="Bowl of tomato broth"></div><div class="item-info"><p class="item-name">Ladle House</p><p class="item-place">Old Town, Spain</p><p class="item-rating"><span class="star">★</span> <b>5.0</b> (210 ratings)</p><p class="item-price">$ 25.00</p></div><svg class="fav" viewBox="0 0 24 22"><use href="#i-heart"/></svg></div>
    <div class="item" style="top:294px"><div class="item-photo tone-d" role="img" aria-label="Bowl of red curry soup"></div><div class="item-info"><p class="item-name">Ladle House</p><p class="item-place">Old Town, Spain</p><p class="item-rating"><span class="star">★</span> <b>5.0</b> (210 ratings)</p><p class="item-price">$ 18.00</p></div><svg class="fav on" viewBox="0 0 24 22"><use href="#i-heart"/></svg></div>
    <div class="item" style="top:368px"><div class="item-photo tone-e" role="img" aria-label="Bowl of creamy chowder"></div><div class="item-info"><p class="item-name">Ladle House</p><p class="item-place">Old Town, Spain</p><p class="item-rating"><span class="star">★</span> <b>5.0</b> (210 ratings)</p><p class="item-price">$ 28.00</p></div><svg class="fav" viewBox="0 0 24 22"><use href="#i-heart"/></svg></div>
    <nav class="tabbar"><svg viewBox="0 0 24 24"><use href="#i-home"/></svg><svg viewBox="0 0 24 24"><use href="#i-search"/></svg><span class="gap"></span><svg viewBox="0 0 24 22"><use href="#i-heart"/></svg><svg viewBox="0 0 24 24"><use href="#i-gear"/></svg></nav>
    <div class="raised" style="left:95px;top:423px"><svg viewBox="0 0 24 24"><use href="#i-bowl"/></svg></div>
  </section>

  <!-- Soup special list -->
  <section class="screen" style="left:848px;top:75px">
    <div class="status"><span>9:41</span><span class="status-icons"><svg viewBox="0 0 34 10" width="26"><use href="#i-signal"/></svg></span></div>
    <div class="pill" style="top:34px">SOUP SPECIAL NAME</div>
    <div class="item" style="top:72px"><div class="item-photo tone-a" role="img" aria-label="Vegetable stew with potatoes"></div><div class="item-info"><p class="item-name">Ladle House</p><p class="item-place">Old Town, Spain</p><p class="item-rating"><span class="star">★</span> <b>5.0</b> (210 ratings)</p><p class="item-price">$ 8.00</p></div><svg class="fav" viewBox="0 0 24 22"><use href="#i-heart"/></svg></div>
    <div class="item" style="top:146px"><div class="item-photo tone-b" role="img" aria-label="Bowl of pumpkin soup with bread"></div><div class="item-info"><p class="item-name">Ladle House</p><p class="item-place">Old Town, Spain</p><p class="item-rating"><span class="star">★</span> <b>5.0</b> (210 ratings)</p><p class="item-price">$ 12.00</p></div><svg class="fav on" viewBox="0 0 24 22"><use href="#i-heart"/></svg></div>
    <div class="item" style="top:220px"><div class="item-photo tone-c" role="img" aria-label="Bowl of tomato broth"></div><div class="item-info"><p class="item-name">Ladle House</p><p class="item-place">Old Town, Spain</p><p class="item-rating"><span class="star">★</span> <b>5.0</b> (210 ratings)</p><p class="item-price">$25.00</p></div><svg class="fav" viewBox="0 0 24 22"><use href="#i-heart"/></svg></div>
    <div class="item" style="top:294px"><div class="item-photo tone-d" role="img" aria-label="Bowl of red curry soup"></div><div class="item-info"><p class="item-name">Ladle House</p><p class="item-place">Old Town, Spain</p><p class="item-rating"><span class="star">★</span> <b>5.0</b> (210 ratings)</p><p class="item-price">$ 18.00</p></div><svg class="fav on" viewBox="0 0 24 22"><use href="#i-heart"/></svg></div>
    <div class="item" style="top:368px"><div class="item-photo tone-e" role="img" aria-label="Bowl of creamy chowder"></div><div class="item-info"><p class="item-name">Ladle House</p><p class="item-place">Old Town, Spain</p><p class="item-rating"><span class="star">★</span> <b>5.0</b> (210 ratings)</p><p class="item-price">$ 28.00</p></div><svg class="fav" viewBox="0 0 24 22"><use href="#i-heart"/></svg></div>
    <nav class="tabbar"><svg viewBox="0 0 24 24"><use href="#i-home"/></svg><svg viewBox="0 0 24 24"><use href="#i-search"/></svg><span class="gap"></span><svg viewBox="0 0 24 22"><use href="#i-heart"/></svg><svg viewBox="0 0 24 24"><use href="#i-gear"/></svg></nav>
    <div class="raised" style="left:95px;top:423px"><svg viewBox="0 0 24 24"><use href="#i-bowl"/></svg></div>
  </section>

  <!-- Cafe profile -->
  <section class="screen" style="left:138px;top:647px">
    <div class="status"><span>9:41</span><span class="status-icons"><svg viewBox="0 0 34 10" width="26"><use href="#i-signal"/></svg></span></div>
    <div class="pill" style="top:34px">CAFE COPPER POT SHOP</div>
    <div class="hero tone-street" role="img" aria-label="Cafe terrace with outdoor tables"></div>
    <div class="pager"><span class="on"></span><span></span><span></span></div>
    <div class="info"><p>NAME :</p><p>ADDRESS :</p><p>SHORT DESCRIPTION :</p></div>
    <p class="group" style="top:264px">SOUPS <svg viewBox="0 0 6 4"><path d="M.5.5 3 3 5.5.5"/></svg></p>
    <div class="row" style="top:276px"><div class="row-photo tone-d" role="img" aria-label="Carrot soup"></div><div class="row-info"><p class="row-name">CARROT + CORIANJER</p><p class="row-qty">1 PCS</p></div><p class="row-price">$ 8.00</p></div>
    <div class="row" style="top:314px"><div class="row-photo tone-c" role="img" aria-label="Chicken ramen"></div><div class="row-info"><p class="row-name">CHICKEN RAMEN</p><p class="row-qty">1 PCS</p></div><p class="row-price">$ 8.00</p></div>
    <p class="group" style="top:355px">SPECIALS <svg viewBox="0 0 6 4"><path d="M.5.5 3 3 5.5.5"/></svg></p>
    <div class="row" style="top:367px"><div class="row-photo tone-d" role="img" aria-label="Sweet potato fritters"></div><div class="row-info"><p class="row-name">SWEET POTATO FRITTERS</p><p class="row-qty">1 PCS</p></div><p class="row-price">$ 8.00</p></div>
    <div class="row" style="top:405px"><div class="row-photo tone-d" role="img" aria-label="Chicken ramen"></div><div class="row-info"><p class="row-name">CHICKEN RAMEN</p><p class="row-qty">1 PCS</p></div><p class="row-price">$ 8.00</p></div>
    <nav class="tabbar"><svg viewBox="0 0 24 24"><use href="#i-home"/></svg><svg viewBox="0 0 24 24"><use href="#i-search"/></svg><svg viewBox="0 0 24 24"><use href="#i-bowl"/></svg><svg viewBox="0 0 24 22"><use href="#i-heart"/></svg><svg viewBox="0 0 24 24"><use href="#i-gear"/></svg></nav>
  </section>

  <!-- Soup and specials availability -->
  <section class="screen" style="left:494px;top:647px">
    <div class="status"><span>9:41</span><span class="status-icons"><svg viewBox="0 0 34 10" width="26"><use href="#i-signal"/></svg></span></div>
    <div class="pill" style="top:34px">SOUP</div>
    <div class="item" style="top:72px"><div class="item-photo tone-a" role="img" aria-label="Vegetable stew with potatoes"></div><div class="item-info"><p class="item-name">Ladle House</p><p class="item-place">Old Town, Spain</p><p class="item-rating"><span class="star">★</span> <b>5.0</b> (210 ratings)</p></div><svg class="fav" viewBox="0 0 24 22"><use href="#i-heart"/></svg><span class="dot go"></span></div>
    <div class="item" style="top:146px"><div class="item-photo tone-b" role="img" aria-label="Bowl of pumpkin soup with bread"></div><div class="item-info"><p class="item-name">Ladle House</p><p class="item-place">Old Town, Spain</p><p class="item-rating"><span class="star">★</span> <b>5.0</b> (210 ratings)</p></div><svg class="fav on" viewBox="0 0 24 22"><use href="#i-heart"/></svg><span class="dot go"></span></div>
    <div class="item" style="top:219px"><div class="item-photo tone-b" role="img" aria-label="Bowl of pumpkin soup with bread"></div><div class="item-info"><p class="item-name">Ladle House</p><p class="item-place">Old Town, Spain</p><p class="item-rating"><span class="star">★</span> <b>5.0</b> (210 ratings)</p></div><svg class="fav on" viewBox="0 0 24 22"><use href="#i-heart"/></svg><span class="dot stop"></span></div>
    <div class="pill" style="top:296px">SPECIAL</div>
    <div class="item" style="top:333px"><div class="item-photo tone-d" role="img" aria-label="Bowl of red curry soup"></div><div class="item-info"><p class="item-name">Ladle House</p><p class="item-place">Old Town, Spain</p><p class="item-rating"><span class="star">★</span> <b>5.0</b> (210 ratings)</p></div><svg class="fav on" viewBox="0 0 24 22"><use href="#i-heart"/></svg><span class="dot stop"></span></div>
    <div class="item" style="top:409px"><div class="item-photo tone-e" role="img" aria-label="Bowl of creamy chowder"></div><div class="item-info"><p class="item-name">Ladle House</p><p class="item-place">Old Town, Spain</p><p class="item-rating"><span class="star">★</span> <b>5.0</b> (210 ratings)</p></div><svg class="fav" viewBox="0 0 24 22"><use href="#i-heart"/></svg></div>
    <nav class="tabbar"><svg viewBox="0 0 24 24"><use href="#i-home"/></svg><svg viewBox="0 0 24 24"><use href="#i-search"/></svg><svg viewBox="0 0 24 24"><use href="#i-bowl"/></svg><svg viewBox="0 0 24 22"><use href="#i-heart"/></svg><svg viewBox="0 0 24 24"><use href="#i-gear"/></svg></nav>
  </section>

  <!-- Check out -->
  <section class="screen" style="left:848px;top:647px">
    <div class="status"><span>9:41</span><span class="status-icons"><svg viewBox="0 0 34 10" width="26"><use href="#i-signal"/></svg></span></div>
    <div class="pill" style="top:34px">CHECK OUT</div>
    <div class="item" style="top:72px"><div class="item-photo tone-a" role="img" aria-label="Vegetable stew with potatoes"></div><div class="item-info"><p class="item-name">Ladle House</p><p class="item-place">Old Town, Spain</p><p class="item-rating"><span class="star">★</span> <b>5.0</b> (210 ratings)</p><p class="item-price">$ 8.00</p></div><svg class="fav on" viewBox="0 0 24 22"><use href="#i-heart"/></svg><span class="dot go"></span></div>
    <div class="item" style="top:146px"><div class="item-photo tone-b" role="img" aria-label="Bowl of pumpkin soup with bread"></div><div class="item-info"><p class="item-name">Ladle House</p><p class="item-place">Old Town, Spain</p><p class="item-rating"><span class="star">★</span> <b>5.0</b> (210 ratings)</p><p class="item-price">$ 8.00</p></div><svg class="fav on" viewBox="0 0 24 22"><use href="#i-heart"/></svg><span class="dot go"></span></div>
    <div class="pill" style="top:219px">CHOOSE YOUR CAFE</div>
    <div class="est" style="left:10px;top:253px;width:160px">
      <div class="est-photo tone-cafe" role="img" aria-label="Cafe interior"></div>
      <div class="est-info">
        <p class="est-name">Cafe Copper Pot</p>
        <p class="est-place">Old Town, Spain</p>
        <p class="est-dist"><svg viewBox="0 0 8 10"><use href="#i-pin"/></svg>2 km to cafe</p>
        <p class="est-stars">★★★★★</p>
        <p class="est-price">$ 8.00</p>
      </div>
    </div>
    <div class="est" style="left:180px;top:253px;width:60px">
      <div class="est-photo tone-street" role="img" aria-label="Cafe terrace on a street"></div>
    </div>
    <div class="map" style="top:327px;height:104px" role="img" aria-label="Street map showing nearby cafes"></div>
    <nav class="tabbar"><svg viewBox="0 0 24 24"><use href="#i-home"/></svg><svg viewBox="0 0 24 24"><use href="#i-search"/></svg><svg viewBox="0 0 24 24"><use href="#i-bowl"/></svg><svg viewBox="0 0 24 22"><use href="#i-heart"/></svg><svg viewBox="0 0 24 24"><use href="#i-gear"/></svg></nav>
  </section>

</main>
</body>
</html>
```